I'm an electrician and the name of my company is called Brisk 'N' Bright Electrical. I require a professional business card that speaks to my clients, I also need it to be innovative and modern. We do maintenance & service work for domestic and commercial premises.

Industry/Entity Type

Electrical

Contact Information for Business Card

Must have the name of my company Brisk 'N' Bright Electrical, my name Darren Kolovos and my contact details 0427 381 592 and company email address Brisknbrightelectrical@mailvane.com and/or website Brisknbrightelectrical.com.au

Logo Text

Brisk 'N' Bright Electrical (If possible)

Colors
33a6d7
0592cd
3176b5

```html
<!DOCTYPE html>
<html lang="en">
<head>
<meta charset="utf-8">
<title>Brisk 'N' Bright Electrical – Business Card</title>
<link rel="stylesheet" href="https://fonts.googleapis.com/css2?family=Montserrat:wght@700&family=Open+Sans:wght@400;600&display=swap">
<style>
  :root {
    --page-bg: #1c1c1c;
    --card-bg: #0b0b0b;
    --accent: #0592cd;
    --accent-light: #33a6d7;
    --accent-deep: #3176b5;
    --text-light: #ffffff;
    --silver: #cfcfcf;
    --divider: #3a3a3a;
  }
  * { box-sizing: border-box; margin: 0; padding: 0; }
  html, body { width: 1200px; height: 900px; overflow: hidden; }
  body {
    background: var(--page-bg);
    display: flex;
    align-items: center;
    justify-content: center;
    gap: 40px;
  }
  .card {
    width: 540px;
    height: 310px;
    background: var(--card-bg);
    border-radius: 18px;
    position: relative;
    overflow: hidden;
  }
  /* Front */
  .card-front { display: flex; align-items: center; }
  .brand-block {
    width: 250px;
    display: flex;
    flex-direction: column;
    align-items: center;
    gap: 14px;
    padding-left: 20px;
  }
  .brand-square {
    width: 34px;
    height: 34px;
    background: var(--accent);
  }
  .brand-name {
    font-family: "Montserrat", sans-serif;
    font-weight: 700;
    font-size: 19px;
    line-height: 1.2;
    text-transform: uppercase;
    text-align: center;
    color: var(--text-light);
    letter-spacing: 0.5px;
  }
  .divider {
    width: 1px;
    height: 180px;
    background: var(--divider);
  }
  .details { padding-left: 26px; }
  .person-name {
    font-family: "Montserrat", sans-serif;
    font-weight: 700;
    font-size: 19px;
    color: var(--accent-light);
    text-transform: uppercase;
    margin-bottom: 26px;
  }
  .contact-list { list-style: none; display: flex; flex-direction: column; gap: 7px; }
  .contact-item {
    display: flex;
    align-items: center;
    gap: 8px;
    font-family: "Open Sans", sans-serif;
    font-size: 12.5px;
    color: var(--text-light);
    white-space: nowrap;
  }
  .contact-icon { width: 14px; height: 14px; flex: none; color: var(--accent); }
  .web-domain { color: var(--accent-light); }
  /* Back */
  .card-back {
    display: flex;
    flex-direction: column;
    align-items: center;
    justify-content: center;
    gap: 16px;
  }
  .card-back .brand-square { background: var(--silver); width: 44px; height: 44px; }
  .card-back .brand-name { color: var(--silver); font-size: 24px; }
</style>
</head>
<body>
  <section class="card card-front">
    <div class="brand-block">
      <span class="brand-square"></span>
      <p class="brand-name">Brisk 'N' Bright<br>Electrical</p>
    </div>
    <span class="divider"></span>
    <div class="details">
      <h1 class="person-name">Darren Kolovos</h1>
      <ul class="contact-list">
        <li class="contact-item">
          <svg class="contact-icon" viewBox="0 0 24 24" aria-hidden="true"><path fill="currentColor" d="M6.6 10.8a15.1 15.1 0 0 0 6.6 6.6l2.2-2.2a1 1 0 0 1 1-.25 11.4 11.4 0 0 0 3.6.57 1 1 0 0 1 1 1V20a1 1 0 0 1-1 1A17 17 0 0 1 3 4a1 1 0 0 1 1-1h3.5a1 1 0 0 1 1 1c0 1.25.2 2.45.57 3.57a1 1 0 0 1-.25 1z"/></svg>
          0427 381 592
        </li>
        <li class="contact-item">
          <svg class="contact-icon" viewBox="0 0 24 24" aria-hidden="true"><path fill="currentColor" d="M2 5h20v14H2z"/><path fill="none" stroke="#0b0b0b" stroke-width="1.6" d="M2 5l10 8 10-8"/></svg>
          Brisknbrightelectrical@mailvane.com
        </li>
        <li class="contact-item">
          <svg class="contact-icon" viewBox="0 0 24 24" aria-hidden="true"><g fill="none" stroke="currentColor" stroke-width="1.8"><circle cx="12" cy="12" r="9.5"/><ellipse cx="12" cy="12" rx="4" ry="9.5"/><path d="M2.5 12h19M4 7h16M4 17h16"/></g></svg>
          <span>www.<span class="web-domain">brisknbrightelectrical</span>.com.au</span>
        </li>
      </ul>
    </div>
  </section>

  <section class="card card-back">
    <span class="brand-square"></span>
    <p class="brand-name">Brisk 'N' Bright<br>Electrical</p>
  </section>
</body>
</html>
```